Website for an electrical contractor :)

We are after a web site which can show pictures of our jobs and our capability in a professional, creative and easily understood way.

----- Brightmoor Electrical ------

We really want a visually good looking website with three sections

Section one:
'Completed projects'
We have a few pictures of jobs which we've completed and would like to show off with a brief description. (see uploads)

Section two:
'Our capabilities'
Just a list of what services we offer

Section three:
We would like a 'contact us' section which people can send us a short msg and upload a file for plans to be able to send to us. We would need their name, phone number and email details. We would also need a short privacy policy saying 'we do not disclose information to third parties'.
We also want to display our contact number and postal address

Good luck :)

Target Market(s)

Adults 25 years+
Business owners
Builders
Real estate agents

Industry/Entity Type

Electrical

Colors

Designer to choose colors to be used in the design.

Requirements
Must have
• Visually appealing
Easy to understand
In the 'Completed projects' section, must have a list for each project we do i can upload pictures for it.

```html
<!DOCTYPE html>
<html lang="en">
<head>
<meta charset="utf-8">
<title>Brightmoor Electrical</title>
<link href="https://fonts.googleapis.com/css2?family=Open+Sans:wght@400;600;700&display=swap" rel="stylesheet">
<style>
:root{
  --red:#e01f26;
  --dark:#111;
  --grey-bar:#5b5b5b;
  --light:#efefef;
  --text:#333;
  --muted:#666;
  --field:#f1f1f1;
}
*{box-sizing:border-box;margin:0;padding:0}
html,body{width:768px;height:1200px;overflow:hidden;background:#fff}
body{font-family:'Open Sans',sans-serif;color:var(--text);position:relative}
.abs{position:absolute}
.header{left:0;top:0;width:768px;height:58px;background:#f2f2f2}
.brand{display:flex;align-items:center;gap:6px}
.brand-dot{width:12px;height:12px;border-radius:50%;background:var(--red)}
.brand-name{font-size:25px;color:#444;font-weight:400;line-height:1}
.brand-sub{font-size:4.5px;color:#666;margin-left:18px;margin-top:1px}
.phone{right:103px;top:11px;display:flex;align-items:center;gap:5px;font-size:11.5px;font-weight:600;color:#222}
.icon-sq{width:14px;height:14px;background:var(--red);border-radius:2px;display:flex;align-items:center;justify-content:center}
.search{left:535px;top:29px;width:130px;height:17px;display:flex}
.search-field{flex:1;background:#fff;font-size:5.5px;color:#999;padding:5px 9px}
.search-btn{width:20px;background:var(--red);display:flex;align-items:center;justify-content:center}
.nav{left:0;top:58px;width:768px;height:24px;background:var(--grey-bar)}
.nav a{position:absolute;top:3px;height:17px;line-height:17px;font-size:6.5px;color:#fff;text-decoration:none}
.nav a.active{background:var(--red);width:48px;text-align:center;font-weight:600}
.soc{position:absolute;top:4px;width:14px;height:14px;background:#888}
.soc.red{background:var(--red)}
.hero{left:0;top:82px;width:768px;height:238px;background:linear-gradient(180deg,#d8d4cc 0%,#c7beb0 45%,#8f887d 75%,#6c6760 100%)}
.hero-line{left:0;top:319px;width:768px;height:2px;background:var(--red)}
.hero-tag1{left:529px;top:170px;width:135px;height:29px;background:var(--red);color:#fff;font-size:18.5px;font-weight:700;text-align:center;line-height:29px;letter-spacing:.3px}
.hero-amp{left:538px;top:210px;color:#fff;font-size:14px;font-weight:700}
.hero-tag2{left:554px;top:204px;width:110px;height:29px;background:#4a4a4a;color:#fff;font-size:15px;font-weight:700;text-align:center;line-height:29px}
.dots{left:360px;top:308px;width:49px;height:24px;background:var(--red);border-radius:4px 4px 0 0;display:flex;gap:5px;align-items:center;justify-content:center}
.dots i{width:7px;height:7px;border:1px solid #fff;border-radius:50%}
.dots i.on{background:#fff}
.sec-title{width:768px;text-align:center;font-size:15px;font-weight:600}
.card{width:129px}
.card-img{width:129px;height:78px;border:1px solid #ddd;padding:3px;background:#fff}
.card-img div{width:100%;height:100%}
.card h3{font-size:8.6px;font-weight:400;margin-top:10px;color:#222;white-space:nowrap}
.card p{font-size:5.3px;color:var(--muted);line-height:8.6px;margin-top:6px}
.btn{display:inline-block;width:48px;height:19px;line-height:19px;text-align:center;font-size:5.8px;font-weight:700;color:#fff;background:var(--red);margin-top:10px}
.btn.dark{background:var(--dark)}
.cap-band{left:0;top:562px;width:768px;height:436px;background:var(--light)}
.cap-img{border:1px solid #ccc;background:#fff;padding:5px;height:173px}
.cap-img div{width:100%;height:100%}
.cap-h{font-size:12px;font-weight:400;color:#222;white-space:nowrap}
.list{list-style:none;width:140px}
.list li{font-size:5.4px;font-weight:600;color:#333;height:14.4px;line-height:9px;padding-left:8px;position:relative;white-space:nowrap}
.list li::before{content:"";position:absolute;left:0;top:3px;width:3px;height:3px;background:#444}
.list li.hl{background:var(--red);color:#fff;height:9px;margin-bottom:5.4px;padding-left:13px}
.list li.hl::before{background:#fff;left:3px}
.f-h{font-size:13px;font-weight:600;color:var(--red)}
.f-text{font-size:5.5px;color:var(--muted);line-height:8.5px}
.info-row{display:flex;gap:7px;font-size:6.5px;color:#444;margin-bottom:8px;align-items:flex-start}
.info-row svg{flex:none;margin-top:1px}
.field{width:178px;height:14px;background:var(--field);font-size:5.3px;color:#777;padding:3px 5px;margin-bottom:5.5px}
.field.area{height:33px}
.fbtn{position:absolute;top:1145px;width:82px;height:19px;background:var(--dark);color:#fff;font-size:6.5px;font-weight:700;text-align:center;line-height:19px}
.fcircle{position:absolute;top:1139px;width:14px;height:14px;border-radius:50%;background:#999}
.footer-line{left:0;top:1175px;width:768px;height:1px;background:#ddd}
.copy{left:105px;top:1183px;font-size:5.3px;color:var(--red)}
</style>
</head>
<body>

<header class="abs header">
  <div class="abs brand" style="left:103px;top:12px">
    <span class="brand-dot"></span>
    <span class="brand-name">Brightmoor</span>
  </div>
  <div class="abs brand-sub" style="left:122px;top:38px">Electrical &amp; Communications &nbsp; EC5128</div>
  <div class="abs phone">04 5521 0386
    <span class="icon-sq"><svg width="8" height="8" viewBox="0 0 24 24"><path fill="#fff" d="M6.6 10.8a15 15 0 0 0 6.6 6.6l2.2-2.2c.3-.3.7-.4 1-.2 1.1.4 2.3.6 3.6.6.6 0 1 .4 1 1V20c0 .6-.4 1-1 1A17 17 0 0 1 3 4c0-.6.4-1 1-1h3.5c.6 0 1 .4 1 1 0 1.3.2 2.5.6 3.6.1.3 0 .7-.2 1z"/></svg></span>
  </div>
  <div class="abs search">
    <div class="search-field">Search here...</div>
    <div class="search-btn"><svg width="8" height="8" viewBox="0 0 24 24"><circle cx="10" cy="10" r="6" fill="none" stroke="#fff" stroke-width="3"/><path d="M15 15l6 6" stroke="#fff" stroke-width="3"/></svg></div>
  </div>
</header>

<nav class="abs nav">
  <a class="active" style="left:103px">Home</a>
  <a style="left:173px">About Us</a>
  <a style="left:236px">Our Projects</a>
  <a style="left:310px">Our Capabilities</a>
  <a style="left:395px">Blog</a>
  <a style="left:444px">Contact Us</a>
  <span class="soc red" style="left:611px"></span>
  <span class="soc" style="left:631px"></span>
  <span class="soc" style="left:651px"></span>
</nav>

<div class="abs hero" role="img" aria-label="Photo of a finished lounge room interior with armchairs and lighting"></div>
<div class="abs hero-tag1">Development</div>
<div class="abs hero-amp">&amp;</div>
<div class="abs hero-tag2">Installation</div>
<div class="abs hero-line"></div>
<div class="abs dots"><i></i><i class="on"></i><i></i></div>

<h2 class="abs sec-title" style="top:346px;color:var(--red)">Our Projects</h2>

<div class="abs card" style="left:103px;top:383px">
  <div class="card-img"><div role="img" aria-label="Project photo: kitchen interior" style="background:linear-gradient(#d97a72,#b9504a)"></div></div>
  <h3 style="color:var(--red)">Lorem Ipsum is simply dummy</h3>
  <p>Lorem Ipsum is simply dummy text of the printing and typesetting industry. Lorem Ipsum has been the industry</p>
  <span class="btn dark">Read More</span>
</div>
<div class="abs card" style="left:247px;top:383px">
  <div class="card-img"><div role="img" aria-label="Project photo: function room" style="background:linear-gradient(#cfcac2,#6e6a64)"></div></div>
  <h3>Lorem Ipsum is simply dummy</h3>
  <p>Lorem Ipsum is simply dummy text of the printing and typesetting industry. Lorem Ipsum has been the industry</p>
  <span class="btn">Read More</span>
</div>
<div class="abs card" style="left:391px;top:383px">
  <div class="card-img"><div role="img" aria-label="Project photo: lounge seating area" style="background:linear-gradient(#d9d6cf,#8d877d)"></div></div>
  <h3>Lorem Ipsum is simply dummy</h3>
  <p>Lorem Ipsum is simply dummy text of the printing and typesetting industry. Lorem Ipsum has been the industry</p>
  <span class="btn">Read More</span>
</div>
<div class="abs card" style="left:535px;top:383px">
  <div class="card-img"><div role="img" aria-label="Project photo: warehouse under construction" style="background:linear-gradient(#3f444a,#8b8f88 60%,#a39a86)"></div></div>
  <h3>Lorem Ipsum is simply dummy</h3>
  <p>Lorem Ipsum is simply dummy text of the printing and typesetting industry. Lorem Ipsum has been the industry</p>
  <span class="btn">Read More</span>
</div>

<section class="abs cap-band"></section>
<h2 class="abs sec-title" style="top:580px;color:#333">Our Capabilities</h2>

<div class="abs cap-img" style="left:103px;top:615px;width:250px"><div role="img" aria-label="Photo of new residential townhouses with paved driveway" style="background:linear-gradient(#4f86c6 0%,#8fb3d8 40%,#6d6a66 55%,#9a948a 100%)"></div></div>
<div class="abs cap-img" style="left:391px;top:615px;width:274px"><div role="img" aria-label="Photo of a commercial concrete building" style="background:linear-gradient(#1f55a8 0%,#4d7fc4 35%,#d4d2cc 55%,#bdb9b0 100%)"></div></div>

<h3 class="abs cap-h" style="left:103px;top:800px">Residential Capability Statement</h3>
<h3 class="abs cap-h" style="left:391px;top:800px">Commercial / Industrial Capability Statement</h3>

<ul class="abs list" style="left:103px;top:823px">
  <li class="hl">24hr Support / faults</li><li>Mains/sub mains cabling</li><li>RCD (Safety Switch) installations</li><li>Smoke alarms</li><li>Power points</li><li>Lighting points</li><li>External lighting</li><li>Sensor lighting</li><li>Switching</li><li>Antennas and Arial points</li><li>Dimmers</li>
</ul>
<ul class="abs list" style="left:247px;top:823px">
  <li>Ceiling fans</li><li>Exhaust fans</li><li>Kitchen / Bathroom Projects</li><li>Re-wires</li><li>Smart wiring</li><li>Phone points</li><li>Data points</li><li>Switchboard installations/relocations</li><li>Compliance investigations/inspections</li><li>Concrete and wall chasing</li><li>Temporary builders site power</li>
</ul>
<ul class="abs list" style="left:391px;top:823px">
  <li>24hr Support / faults</li><li>Lighting/power design and consultation</li><li>Emergency and exit lighting</li><li>Led strip lighting</li><li>Energy efficient lighting</li><li>Temporary lighting</li><li>Illuminated signage</li><li>Switchboard relocations</li><li>Maintenance</li><li>RCD installation</li>
</ul>
<ul class="abs list" style="left:535px;top:823px">
  <li>Phone/data points</li><li>Data cabinets</li><li>Data Networking</li><li>IDF installations/relocations</li><li>All power requirements</li><li>All three phase power requirements</li><li>Electrical rip outs / Disconnections</li><li>Thermal Imaging scans</li><li>Commercial lighting</li><li>Concrete and wall chasing</li>
</ul>

<footer>
  <div class="abs brand" style="left:103px;top:1023px">
    <span class="brand-dot"></span>
    <span class="brand-name">Brightmoor</span>
  </div>
  <div class="abs brand-sub" style="left:122px;top:1049px">Electrical &amp; Communications &nbsp; EC5128</div>
  <p class="abs f-text" style="left:103px;top:1067px;width:130px">Lorem Ipsum is simply dummy text of the printing and typesetting industry. Lorem Ipsum has been the industry's standard dummy text ever since</p>
  <h4 class="abs f-h" style="left:103px;top:1110px">Follow Us On</h4>
  <span class="fcircle" style="left:103px;background:#2f5fa8"></span>
  <span class="fcircle" style="left:123px"></span>
  <span class="fcircle" style="left:143px"></span>

  <h4 class="abs f-h" style="left:295px;top:1018px">Contact Info</h4>
  <div class="abs" style="left:295px;top:1044px;width:180px">
    <div class="info-row"><svg width="6" height="6" viewBox="0 0 24 24"><path fill="#444" d="M6.6 10.8a15 15 0 0 0 6.6 6.6l2.2-2.2c.3-.3.7-.4 1-.2 1.1.4 2.3.6 3.6.6.6 0 1 .4 1 1V20c0 .6-.4 1-1 1A17 17 0 0 1 3 4c0-.6.4-1 1-1h3.5c.6 0 1 .4 1 1 0 1.3.2 2.5.6 3.6.1.3 0 .7-.2 1z"/></svg><span>04 5521 0386</span></div>
    <div class="info-row"><svg width="6" height="6" viewBox="0 0 24 24"><rect x="6" y="2" width="12" height="6" fill="#444"/><rect x="2" y="9" width="20" height="9" fill="#444"/><rect x="6" y="15" width="12" height="7" fill="#fff" stroke="#444" stroke-width="2"/></svg><span>08 9312 4058</span></div>
    <div class="info-row"><svg width="6" height="6" viewBox="0 0 24 24"><rect x="2" y="5" width="20" height="14" fill="#444"/><path d="M2 5l10 8 10-8" fill="none" stroke="#fff" stroke-width="2"/></svg><span>info@brightmoorelectrical.com.au</span></div>
    <div class="info-row"><svg width="6" height="7" viewBox="0 0 24 28"><path fill="#444" d="M12 0a9 9 0 0 0-9 9c0 7 9 19 9 19s9-12 9-19a9 9 0 0 0-9-9zm0 12a3 3 0 1 1 0-6 3 3 0 0 1 0 6z"/></svg><span>P.O Box 117 Harbour View W.A<br>6031 A.B.N: 48 203 917 552</span></div>
  </div>

  <h4 class="abs f-h" style="left:487px;top:1018px">Contact From</h4>
  <div class="abs" style="left:487px;top:1047px">
    <div class="field">Enter Your Name :</div>
    <div class="field">Enter Your Phone :</div>
    <div class="field">Enter Your Email :</div>
    <div class="field area">Massage :</div>
  </div>
  <span class="fbtn" style="left:487px">Upload File</span>
  <span class="fbtn" style="left:583px;color:var(--red)">Submit</span>

  <div class="abs footer-line"></div>
  <p class="abs copy">All Copyrigts Reserved © Brightmoor Electrical 2015. Privacy Policy</p>
</footer>

</body>
</html>
```